KVT Business Cards

We require business cards for our business. We would like a matte black back to the card, with our logo centred in the middle. The front side of the card is open to design.

Target Market(s)

Clients looking for legal services (professional)

Industry/Entity Type

Legal

Contact Information for Business Card

Boris Telemark
Partner
Mobile: 0438 715 642
Email: boris@kvtlaw.co
Website: www.kvtlaw.co
Level 3, 118 Wexbury Street
Sydney NSW 2000

Font styles to use
Other font styles liked:
• Avenir

Colors
f04a50
ffffff
1b1b1b

Requirements
Must have
• Black back with logo included in the centre of the card.
• Our font is Avenir.

```html
<!DOCTYPE html>
<html lang="en">
<head>
<meta charset="utf-8">
<title>KVT Legal Business Cards</title>
<link href="https://fonts.googleapis.com/css2?family=Nunito+Sans:wght@400;600;700;800&display=swap" rel="stylesheet">
<style>
  :root {
    --card-black: #1b1b1b;
    --brand-red: #d8224a;
    --white: #ffffff;
    --muted: #d9d9d9;
    --stage: #2b2e33;
  }
  * { margin: 0; padding: 0; box-sizing: border-box; }
  html, body {
    width: 1200px; height: 900px; overflow: hidden;
    background: var(--stage);
    font-family: "Nunito Sans", "Avenir", sans-serif;
    color: var(--white);
  }
  .canvas {
    position: relative; width: 1200px; height: 900px;
  }
  .card {
    position: absolute;
    width: 525px; height: 300px;
    border-radius: 26px;
    background: var(--card-black);
    overflow: hidden;
    box-shadow: 0 18px 40px rgba(0,0,0,.45);
  }
  .card--front { left: 50px; top: 300px; }
  .card--back  { left: 625px; top: 300px; }

  /* front */
  .front__band {
    position: absolute; left: 0; right: 0; bottom: 0; height: 14px;
    background: var(--brand-red);
  }
  .front__name {
    position: absolute; left: 36px; top: 34px;
    font-size: 25px; font-weight: 600; letter-spacing: .5px;
    text-transform: uppercase;
  }
  .front__role {
    position: absolute; left: 36px; top: 66px;
    font-size: 14px; font-weight: 400; letter-spacing: 1px;
    color: var(--brand-red); text-transform: uppercase;
  }
  .front__rule {
    position: absolute; left: 36px; right: 36px; top: 104px;
    height: 1px; background: var(--muted);
  }
  .front__contacts {
    position: absolute; left: 36px; top: 122px;
    list-style: none; font-size: 15px; line-height: 27px;
  }
  .front__contacts li { display: flex; align-items: center; gap: 10px; }
  .front__contacts svg { width: 11px; height: 11px; flex: none; }
  .front__address {
    position: absolute; right: 36px; bottom: 44px;
    text-align: right; font-size: 17px; line-height: 28px;
  }
  .brand {
    position: absolute; display: flex; align-items: center; gap: 12px;
  }
  .brand__square { width: 16px; height: 16px; background: var(--brand-red); }
  .brand__name {
    font-weight: 800; text-transform: uppercase; letter-spacing: 1px;
    color: var(--white);
  }
  .card--front .brand { right: 36px; top: 38px; }
  .card--front .brand__name { font-size: 24px; }

  /* back */
  .card--back .brand {
    left: 50%; top: 50%; transform: translate(-50%, -70%);
  }
  .card--back .brand__square { width: 24px; height: 24px; }
  .card--back .brand__name { font-size: 40px; }
  .back__url {
    position: absolute; left: 0; right: 0; top: 190px;
    text-align: center; font-size: 13px; font-weight: 600;
    letter-spacing: 3px; color: var(--muted);
  }
</style>
</head>
<body>
<main class="canvas">

  <section class="card card--front" aria-label="Business card front">
    <div class="front__name">Boris Telemark</div>
    <div class="front__role">Partner</div>
    <div class="brand">
      <span class="brand__square"></span>
      <span class="brand__name">KVT Legal</span>
    </div>
    <div class="front__rule"></div>
    <ul class="front__contacts">
      <li>
        <svg viewBox="0 0 11 11" aria-hidden="true"><rect x="2.5" y="0.5" width="6" height="10" rx="1.2" fill="none" stroke="#d8224a" stroke-width="1.2"/></svg>
        0438 715 642
      </li>
      <li>
        <svg viewBox="0 0 11 11" aria-hidden="true"><rect x="0.5" y="2" width="10" height="7" rx="1" fill="#d8224a"/></svg>
        boris@kvtlaw.co
      </li>
      <li>
        <svg viewBox="0 0 11 11" aria-hidden="true"><circle cx="5.5" cy="5.5" r="5" fill="#d8224a"/></svg>
        www.kvtlaw.co
      </li>
    </ul>
    <address class="front__address" style="font-style:normal">
      Level 3, 118 Wexbury Street<br>
      Sydney NSW 2000
    </address>
    <div class="front__band"></div>
  </section>

  <section class="card card--back" aria-label="Business card back">
    <div class="brand">
      <span class="brand__square"></span>
      <span class="brand__name">KVT Legal</span>
    </div>
    <div class="back__url">WWW.KVTLAW.CO</div>
  </section>

</main>
</body>
</html>
```